Brindlewood Holdings LLC - Business Cards

Need the following information on the cards:

Name: Marcus T Velding
Title: Chief Executive Manager

Business address:
412 N Pickerel Ridge Road #118
Carol Stream, Il 60188

Phone: (555) 481-0362 - Business
BRX FFL license number: 5-81-xxx-xx-xx-04519
Email: marcus.velding@brindlewoodholdingsffl.example

Target Market(s)

Firearm owners

Industry/Entity Type

Firearms industry,

Contact Information for Business Card

Contact number, name and title, web page address, email, business address and brx license number,

Requirements
Must have
• Name, title, business address, phone numbers, BRX license numbers, web page address and email address.
Nice to have
• Cellphone number,

```html
<!DOCTYPE html>
<html lang="en">
<head>
<meta charset="utf-8">
<title>Brindlewood Holdings LLC – Business Cards</title>
<link rel="stylesheet" href="https://fonts.googleapis.com/css2?family=Roboto+Slab:wght@300;400;700&display=swap">
<style>
  :root {
    --brand-red: #cf1c23;
    --brand-black: #231f20;
    --paper: #ffffff;
    --ink: #231f20;
    --rule: #9a9a9a;
  }
  * { box-sizing: border-box; margin: 0; padding: 0; }
  html, body {
    width: 1200px; height: 1200px; overflow: hidden;
    background: var(--paper);
    font-family: "Roboto Slab", Georgia, serif;
    color: var(--ink);
  }
  .canvas { position: relative; width: 1200px; height: 1200px; }
  .card { position: absolute; left: 156px; width: 896px; overflow: hidden; }
  .card-front { top: 64px; height: 512px; }
  .card-back { top: 631px; height: 513px; border: 1px solid var(--rule); border-right: none; }
  .card-art { position: absolute; inset: 0; display: block; }

  .brand-name {
    position: absolute;
    color: var(--paper);
    font-weight: 700;
    text-transform: uppercase;
    text-align: center;
    line-height: 1.15;
    letter-spacing: 0.06em;
  }
  .card-front .brand-name { left: 248px; width: 400px; top: 150px; font-size: 38px; }
  .card-back .brand-name { left: 506px; width: 340px; top: 212px; font-size: 30px; }

  .holder-name {
    position: absolute; left: 40px; top: 50px;
    font-size: 48px; line-height: 56px; font-weight: 700; letter-spacing: -0.01em; white-space: nowrap;
  }
  .holder-title {
    position: absolute; left: 42px; top: 108px;
    font-size: 23px; line-height: 28px; font-weight: 300; white-space: nowrap;
  }
  .divider {
    position: absolute; left: 39px; top: 211px; width: 160px; height: 1px;
    background: var(--rule);
  }
  .contact { position: absolute; left: 39px; top: 0; width: 420px; }
  .contact-row {
    position: absolute; left: 0; display: flex; align-items: flex-start;
    font-size: 22px; font-weight: 300; line-height: 27px; white-space: nowrap;
  }
  .contact-icon { width: 20px; height: 20px; margin-top: 3px; margin-right: 20px; flex: none; }
  .row-phone { top: 230px; }
  .row-license { top: 260px; }
  .row-email { top: 302px; }
  .row-web { top: 360px; }
  .row-address { top: 402px; }
</style>
</head>
<body>
<main class="canvas">

  <section class="card card-front" aria-label="Card front">
    <svg class="card-art" viewBox="0 0 896 512" aria-hidden="true">
      <rect width="896" height="512" fill="var(--brand-red)"/>
      <path d="M0 0 H896 V216 C560 433 250 403 0 226 Z" fill="var(--paper)"/>
      <path d="M0 0 H896 V205 C560 420 250 390 0 214 Z" fill="var(--brand-black)"/>
    </svg>
    <p class="brand-name">Brindlewood<br>Holdings LLC</p>
  </section>

  <section class="card card-back" aria-label="Card back">
    <svg class="card-art" viewBox="0 0 896 513" aria-hidden="true">
      <rect width="896" height="513" fill="var(--paper)"/>
      <path d="M504 0 H896 V513 H504 C453 360 453 153 504 0 Z" fill="var(--brand-black)"/>
      <path d="M516 0 H896 V513 H516 C464 360 464 153 516 0 Z" fill="var(--brand-red)"/>
    </svg>

    <h1 class="holder-name">Marcus T Velding</h1>
    <p class="holder-title">Chief Executive Manager</p>
    <div class="divider"></div>

    <div class="contact">
      <div class="contact-row row-phone">
        <svg class="contact-icon" viewBox="0 0 20 20" aria-hidden="true"><rect width="20" height="20" rx="3" fill="var(--ink)"/><path d="M6 4.5 L8 4.5 L9 7.5 L7.6 8.6 C8.3 10.1 9.6 11.5 11.2 12.3 L12.4 11 L15.5 12 L15.5 14 C15.5 14.8 14.8 15.5 14 15.5 C8.8 15.2 4.8 11.2 4.5 6 C4.5 5.2 5.2 4.5 6 4.5 Z" fill="var(--paper)"/></svg>
        <span>+1 555 481 0362</span>
      </div>
      <div class="contact-row row-license">
        <svg class="contact-icon" viewBox="0 0 20 20" aria-hidden="true"><rect width="20" height="20" rx="3" fill="var(--ink)"/><rect x="4" y="6" width="12" height="8.5" rx="1" fill="none" stroke="var(--paper)" stroke-width="1.1"/><circle cx="7.3" cy="9" r="1.2" fill="var(--paper)"/><path d="M5.6 12.6 C5.8 11 8.8 11 9 12.6 Z" fill="var(--paper)"/><path d="M10.5 8.8 H14.5 M10.5 10.6 H14.5 M10.5 12.4 H13.2" stroke="var(--paper)" stroke-width="0.9"/></svg>
        <span>5-81-xxx-xx-xx-04519</span>
      </div>
      <div class="contact-row row-email">
        <svg class="contact-icon" viewBox="0 0 20 20" aria-hidden="true"><rect width="20" height="20" rx="3" fill="var(--ink)"/><rect x="4.5" y="6" width="11" height="8" rx="0.8" fill="none" stroke="var(--paper)" stroke-width="1.2"/><path d="M4.8 6.5 L10 10.6 L15.2 6.5" fill="none" stroke="var(--paper)" stroke-width="1.2"/></svg>
        <span>marcus.velding@<br>brindlewoodholdingsffl.example</span>
      </div>
      <div class="contact-row row-web">
        <svg class="contact-icon" viewBox="0 0 20 20" aria-hidden="true"><rect width="20" height="20" rx="3" fill="var(--ink)"/><g fill="none" stroke="var(--paper)" stroke-width="1"><circle cx="10" cy="10" r="5.5"/><ellipse cx="10" cy="10" rx="2.4" ry="5.5"/><path d="M4.5 10 H15.5 M5.3 7.3 H14.7 M5.3 12.7 H14.7"/></g></svg>
        <span>brindlewoodholdingsffl.example</span>
      </div>
      <div class="contact-row row-address">
        <svg class="contact-icon" viewBox="0 0 20 20" aria-hidden="true"><rect width="20" height="20" rx="3" fill="var(--ink)"/><path d="M10 4 C7.5 4 5.8 5.9 5.8 8.2 C5.8 11.2 10 16 10 16 C10 16 14.2 11.2 14.2 8.2 C14.2 5.9 12.5 4 10 4 Z" fill="var(--paper)"/><circle cx="10" cy="8.2" r="1.6" fill="var(--ink)"/></svg>
        <span>412 N Pickerel Ridge Road<br>#118 Carol Stream,<br>Il 60188</span>
      </div>
    </div>

    <p class="brand-name">Brindlewood<br>Holdings LLC</p>
  </section>

</main>
</body>
</html>
```